Modern Business Card for Lanternfield 2018

Our company assumes the best about people. We are creating an online community of entrepreneurs and business leaders who struggle with marketing their business online.

This business card should POP! We recently got a new logo and are launching a new website next month, so our business cards should make a statement that feels:
-Fresh
-Smart
-Trustworthy
-Fun

Target Market(s)

small business owners, entrepreneurs

Industry/Entity Type

Digital Marketing

Contact Information for Business Card

Dimensions: 3.5" x 2"

Font styles to use
Sans Serif

Colors
f37122
ffffff

Requirements
Must have
• We need a business card with a modern, bold design. We will use one side of the card as a lead-generation offer, so text on one side will need to fit up to 140 characters. The business card should stick to our core colors (orange, black, and white).
Nice to have
• We think a vertical "portrait" design could be interesting.
Should not have
• Should not look like a traditional business card. The round icon should stand out from a distance.

```html
<!DOCTYPE html>
<html lang="en">
<head>
<meta charset="utf-8">
<title>Lanternfield Business Card</title>
<link rel="stylesheet" href="https://fonts.googleapis.com/css2?family=Barlow:wght@400;500;600&family=Open+Sans:wght@800&family=Permanent+Marker&family=Merriweather:ital,wght@1,900&display=swap">
<style>
  :root {
    --orange: #f37122;
    --white: #ffffff;
    --ink: #333132;
    --text-grey: #3a3a3a;
    --backdrop: #dcdcdc;
  }
  * { margin: 0; padding: 0; box-sizing: border-box; }
  html, body { width: 1200px; height: 1200px; overflow: hidden; }
  body { background: var(--backdrop); position: relative; font-family: "Barlow", sans-serif; }

  .card {
    position: absolute;
    left: 219px;
    width: 762px;
    height: 436px;
    display: flex;
    overflow: hidden;
  }
  .card--front { top: 102px; }
  .card--back { top: 627px; }

  .edge-band { width: 25px; height: 100%; }
  .edge-band--ink { background: var(--ink); }
  .edge-band--orange { background: var(--orange); }

  .identity-panel {
    position: relative;
    width: 414px;
    background: var(--white);
  }
  .identity-panel .person-name {
    position: absolute;
    left: 55px;
    top: 218px;
    font-family: "Permanent Marker", cursive;
    font-size: 46px;
    line-height: 56px;
    color: var(--ink);
    letter-spacing: 1px;
    text-transform: uppercase;
  }
  .identity-panel .person-role {
    position: absolute;
    left: 47px;
    top: 340px;
    font-size: 23px;
    font-weight: 500;
    color: var(--text-grey);
  }
  .identity-panel .person-email {
    position: absolute;
    left: 47px;
    top: 371px;
    font-size: 26px;
    font-weight: 400;
    color: var(--text-grey);
    letter-spacing: 0.3px;
  }

  .brand-panel {
    position: relative;
    width: 323px;
    display: flex;
    align-items: center;
    justify-content: center;
  }
  .brand-panel--orange { background: var(--orange); }
  .brand-panel--white { background: var(--white); }

  .brand-disc {
    width: 228px;
    height: 228px;
    border-radius: 50%;
    display: flex;
    align-items: center;
    justify-content: center;
    font-family: "Barlow", sans-serif;
    font-weight: 600;
    font-size: 31px;
  }
  .brand-disc--white { background: var(--white); color: var(--orange); }
  .brand-disc--orange { background: var(--orange); color: var(--white); }

  .offer-panel {
    width: 414px;
    background: var(--ink);
    color: var(--white);
    text-align: center;
    padding-top: 98px;
  }
  .offer-panel .wordmark {
    font-family: "Open Sans", sans-serif;
    font-weight: 800;
    font-size: 43px;
    line-height: 1;
    letter-spacing: 0.5px;
  }
  .offer-panel .tagline {
    margin-top: 12px;
    font-family: "Merriweather", serif;
    font-style: italic;
    font-weight: 900;
    font-size: 19px;
  }
  .offer-panel .lead-offer {
    margin-top: 50px;
    font-size: 19px;
    font-weight: 500;
    line-height: 24px;
  }
  .offer-panel .lead-url {
    margin-top: 6px;
    font-size: 27px;
    font-weight: 500;
    letter-spacing: 0.3px;
  }
</style>
</head>
<body>
  <section class="card card--front" aria-label="Business card front">
    <div class="edge-band edge-band--ink"></div>
    <div class="identity-panel">
      <p class="person-name">Mara<br>Ellison</p>
      <p class="person-role">Story Marketing Coach</p>
      <p class="person-email">mara@lanternfieldnow.com</p>
    </div>
    <div class="brand-panel brand-panel--orange">
      <div class="brand-disc brand-disc--white">Lanternfield</div>
    </div>
  </section>

  <section class="card card--back" aria-label="Business card back">
    <div class="brand-panel brand-panel--white">
      <div class="brand-disc brand-disc--orange">Lanternfield</div>
    </div>
    <div class="offer-panel">
      <h1 class="wordmark">LANTERNFIELD</h1>
      <p class="tagline">Tell Stories That Inspire Action</p>
      <p class="lead-offer">Get your free Lanternfield Starter Package<br>and our marketing guide today at</p>
      <p class="lead-url">lanternfieldnow.com/start</p>
    </div>
    <div class="edge-band edge-band--orange"></div>
  </section>
</body>
</html>
```